Business Card Design Project

I own a dental practice and would like to use a logo that was recently designed to make business cards.
I am looking for a clean card with the following information on the card.

Halvorsen Dental Center (Using the logo)
Martin L. Halvorsen, D.D.S.
7234 Pinewick Ave. Suite B
Colorado Springs, CO 80547
(719) 482-6130
halvorsendentalcenter@mailbox-example.net
www.halvorsendentalcenter.example

Also a list of items on the back:
Services include

Family Dentistry
Cosmetic
Whitening
Tooth Colored Fillings
Crowns/Bridges
Implants/Tooth Replacement
Dentures
Root Canals
Updates

Just an FYI, I added an email address and website address.

I also added my Pic.  Please give designs with and without the pic

Thanks

Target Market(s)

20-70 U.S. Female that handles the household budget.

Industry/Entity Type

Dental

Requirements
Must have
• The logo is key. The color scheme of the logo is also key. The back of the business card should have the list of Dental Services offered at the practice. The front should be clean and professional looking. No cartoons. I will also include a picture of myself. I think that the final card may or may not include this picture, so the card designs should come with and without the picture. USE THE BLUE LOGO ONLY!!!
Should not have
• NO teeth should be on the card.

```html
<!DOCTYPE html>
<html lang="en">
<head>
<meta charset="utf-8">
<title>Halvorsen Dental Center – Business Card</title>
<link rel="stylesheet" href="https://fonts.googleapis.com/css2?family=Open+Sans:wght@400;600&family=Arimo:wght@400&display=swap">
<style>
  :root {
    --bg: #c9cacc;
    --card: #ffffff;
    --ink: #5a5f66;
    --ink-soft: #6d7278;
    --brand: #5b6b78;
    --accent: #4f86a6;
    --accent-light: #8fb5cc;
    --rule: #8a8e93;
    --photo-top: #eeecea;
    --photo-bottom: #2c2d35;
  }
  * { box-sizing: border-box; margin: 0; padding: 0; }
  html, body { width: 1200px; height: 944px; overflow: hidden; }
  body { background: var(--bg); position: relative; font-family: "Open Sans", sans-serif; }

  .card {
    position: absolute;
    width: 620px;
    height: 354px;
    background: var(--card);
    border-radius: 20px;
    overflow: hidden;
    box-shadow: 0 6px 18px rgba(0,0,0,0.18);
  }
  .card--front { left: 70px; top: 70px; }
  .card--back { left: 510px; top: 510px; }

  .portrait { position: absolute; left: 0; top: 0; }

  .brand {
    position: absolute;
    display: flex;
    align-items: center;
    gap: 10px;
    font-family: "Open Sans", sans-serif;
    font-weight: 600;
    color: var(--brand);
    white-space: nowrap;
  }
  .brand__dot {
    width: 26px; height: 26px;
    border-radius: 50%;
    background: var(--accent-light);
    flex: none;
  }
  .card--front .brand { left: 300px; top: 42px; font-size: 22px; }
  .card--back .brand { left: 40px; top: 42px; font-size: 22px; }

  .services {
    position: absolute;
    left: 300px; top: 150px;
    width: 300px;
    list-style: none;
    text-align: center;
    font-size: 15.5px;
    line-height: 25px;
    color: var(--ink);
  }

  .divider {
    position: absolute;
    left: 40px; right: 0; top: 152px;
    border-top: 1.5px solid var(--rule);
  }
  .dentist {
    position: absolute;
    right: 34px; top: 122px;
    text-align: right;
    font-family: "Arimo", sans-serif;
  }
  .dentist__name { font-size: 22px; letter-spacing: 1px; color: var(--accent); line-height: 28px; }
  .dentist__degree { font-size: 15px; color: var(--ink); margin-top: 2px; }

  .contact {
    position: absolute;
    left: 36px; top: 226px;
    list-style: none;
    font-family: "Arimo", sans-serif;
    font-size: 13.5px;
    color: var(--ink);
  }
  .contact li { display: flex; align-items: center; gap: 10px; height: 24px; }
  .contact svg { width: 15px; height: 15px; flex: none; }

  .address {
    position: absolute;
    right: 30px; top: 262px;
    font-family: "Arimo", sans-serif;
    font-size: 13.5px;
    line-height: 22px;
    color: var(--ink);
    text-align: left;
    font-style: normal;
  }
</style>
</head>
<body>

<section class="card card--front">
  <svg class="portrait" width="620" height="354" viewBox="0 0 620 354" role="img" aria-label="Portrait photo of the dentist in a dark suit">
    <defs>
      <linearGradient id="portraitTone" x1="0" y1="0" x2="0" y2="1">
        <stop offset="0" stop-color="var(--photo-top)"/>
        <stop offset="0.45" stop-color="#cbbfb8"/>
        <stop offset="1" stop-color="var(--photo-bottom)"/>
      </linearGradient>
    </defs>
    <path d="M0 0 H160 A235 235 0 0 1 200 354 H0 Z" fill="url(#portraitTone)"/>
    <path d="M160 0 A235 235 0 0 1 200 354" fill="none" stroke="#555" stroke-width="1.5"/>
  </svg>

  <div class="brand"><span class="brand__dot"></span>Halvorsen Dental Center</div>

  <ul class="services">
    <li>• Family Dentistry • Cosmetic</li>
    <li>• Whitening • Tooth Colored Fillings</li>
    <li>• Crowns/Bridges</li>
    <li>• Implants/Tooth Replacement</li>
    <li>• Dentures • Root Canals</li>
  </ul>
</section>

<section class="card card--back">
  <div class="brand"><span class="brand__dot"></span>Halvorsen Dental Center</div>

  <div class="dentist">
    <div class="dentist__name">Martin L. Halvorsen</div>
    <div class="dentist__degree">D.D.S.</div>
  </div>
  <div class="divider"></div>

  <ul class="contact">
    <li>
      <svg viewBox="0 0 16 16" aria-hidden="true"><circle cx="8" cy="8" r="7.5" fill="none" stroke="var(--ink-soft)"/><path d="M5.5 4.5c-.8.8-.6 2.6 1 4.4 1.7 1.8 3.6 2.3 4.4 1.5l-1.4-1.5-1 .6c-.8-.4-1.6-1.2-2-2l.6-1z" fill="var(--ink-soft)"/></svg>
      (719) 482-6130
    </li>
    <li>
      <svg viewBox="0 0 16 16" aria-hidden="true"><circle cx="8" cy="8" r="7.5" fill="var(--ink-soft)"/><rect x="4" y="5.5" width="8" height="5.5" fill="#fff"/><path d="M4 5.5 8 8.5 12 5.5" fill="none" stroke="var(--ink-soft)" stroke-width="0.8"/></svg>
      halvorsendentalcenter@mailbox-example.net
    </li>
    <li>
      <svg viewBox="0 0 16 16" aria-hidden="true"><circle cx="8" cy="8" r="7.5" fill="var(--ink-soft)"/></svg>
      www.halvorsendentalcenter.example
    </li>
  </ul>

  <address class="address">
    7234 Pinewick Ave. Suite B<br>
    Colorado Springs, CO 80547
  </address>
</section>

</body>
</html>
```